Oil & Gas Energy Consultancy Service

I am an experienced Upper Management former employed by a Global Service Company to the Oil & Gas Industry.
After 22 years I have decided to go as a Consultant working mainly in the same,(upper management) areas of work.
This is a, "One Man" operation.
Updates

Thank you all for your interest and professionalism in this little project.

It was hard to decide on a final contestant but it had to come down to one selection.
Best of luck with your other work & projects!
Tavo Ressani-Merrick

Industry/Entity Type

Industry

Contact Information for Business Card

Trelumo Energy Services, Inc
Tavo Ressani-Merrick - Managing Director
O&G Consultants
Suite 4140, Tower 3, Halden Ave, Edmonton, AB, T6K 2P5 Canada
250 555 0194 tavo.merrick@trelumo-example.net

Logo Text

Trelumo Energy Services

Logo styles of interest
Abstract Logo

```html
<!DOCTYPE html>
<html lang="en">
<head>
<meta charset="utf-8">
<title>Trelumo Energy Services – Business Card</title>
<link rel="stylesheet" href="https://fonts.googleapis.com/css2?family=PT+Sans:wght@400;700&display=swap">
<style>
  :root {
    --page-bg: #e6e7e9;
    --card-bg: #f7f8f8;
    --brand-blue: #3d96da;
    --band-blue: #1f62b4;
    --accent-blue: #3a9ad9;
    --ink: #2b2d30;
    --rule: #3a3c40;
    --white: #ffffff;
  }
  * { box-sizing: border-box; margin: 0; padding: 0; }
  html, body {
    width: 1200px;
    height: 800px;
    overflow: hidden;
    background: var(--page-bg);
    font-family: "PT Sans", "Helvetica Neue", Arial, sans-serif;
  }
  .card {
    position: absolute;
    left: 150px;
    top: 143px;
    width: 900px;
    height: 514px;
    background: var(--card-bg);
    box-shadow: 0 6px 18px rgba(0, 0, 0, 0.12);
    overflow: hidden;
  }
  .brand-panel {
    position: absolute;
    left: 80px;
    top: 0;
    width: 360px;
    height: 300px;
    background: var(--brand-blue);
    display: flex;
    flex-direction: column;
    align-items: center;
    justify-content: center;
    gap: 18px;
  }
  .brand-panel::after {
    content: "";
    position: absolute;
    left: 34px;
    bottom: -16px;
    border-right: 18px solid transparent;
    border-top: 16px solid var(--brand-blue);
  }
  .brand-mark {
    width: 120px;
    height: 120px;
    border: 14px solid var(--white);
    border-radius: 50%;
  }
  .brand-name {
    color: var(--white);
    font-size: 30px;
    font-weight: 400;
    letter-spacing: 0.04em;
  }
  .person {
    position: absolute;
    left: 84px;
    top: 318px;
    width: 370px;
  }
  .person-name {
    color: var(--ink);
    font-size: 38px;
    font-weight: 400;
    line-height: 1.1;
    white-space: nowrap;
  }
  .person-title {
    color: var(--accent-blue);
    font-size: 19px;
    letter-spacing: 0.08em;
    text-transform: uppercase;
    margin-top: 4px;
  }
  .divider {
    position: absolute;
    left: 476px;
    top: 236px;
    width: 2px;
    height: 164px;
    background: var(--rule);
  }
  .contact {
    position: absolute;
    left: 500px;
    top: 218px;
    width: 380px;
    color: var(--ink);
  }
  .company-name {
    font-size: 23px;
    font-weight: 400;
    letter-spacing: 0.03em;
    text-transform: uppercase;
    margin-bottom: 12px;
    white-space: nowrap;
  }
  .contact-label {
    color: var(--accent-blue);
    font-size: 13px;
    font-weight: 700;
    letter-spacing: 0.06em;
    text-transform: uppercase;
    margin-top: 10px;
    margin-left: 36px;
  }
  .contact-value {
    font-size: 17px;
    line-height: 1.3;
    margin-left: 36px;
  }
  .contact-label.email-label,
  .contact-value.email { margin-left: 0; }
  .footer-band {
    position: absolute;
    left: 0;
    right: 0;
    bottom: 14px;
    height: 66px;
    background: var(--band-blue);
  }
</style>
</head>
<body>
  <main class="card">
    <div class="brand-panel">
      <div class="brand-mark"></div>
      <div class="brand-name">Trelumo</div>
    </div>

    <div class="person">
      <h1 class="person-name">Tavo Ressani-Merrick</h1>
      <p class="person-title">Managing Director</p>
    </div>

    <div class="divider"></div>

    <section class="contact">
      <h2 class="company-name">Trelumo Energy Services, Inc.</h2>
      <p class="contact-label">Address</p>
      <p class="contact-value">Suite 4140, Tower 3, Halden Ave<br>Edmonton, AB, T6K 2P5 Canada</p>
      <p class="contact-label">Phone</p>
      <p class="contact-value">250 555 0194</p>
      <p class="contact-label email-label">Email</p>
      <p class="contact-value email">tavo.merrick@trelumo-example.net</p>
    </section>

    <div class="footer-band"></div>
  </main>
</body>
</html>
```